Managed Service Provider need new business cards

We are a small Maanged Service Provider of IT Services and need a new fresh design for our business cards. We want something impossible, fun and professional :)
Our services has a large range, but we are always fun and make sure our customers both get their issue sorted and also feel like they are "catching up with an old friend".
All our cards in the past has always been all black, with red and we need something fresher.
The back of card, we would like just a small list of what we do i think, but if someone has a better idea, please do something cool with the back of the card:
Managed IT Services
Productivity Solutions
Data Backup and Recovery
IT System Maintenance
Managed IT Security
More details can be found on our website tqnetworks.com.au
Industry/Entity Type
It Company
Contact Information for Business Card
Name: Dwayne Falstrup
Title: Director
Phone: 03 6193 4827
Mobile: 0412 587 239
Email: dwayne@tqnetworks.com.au
Web: www.tqnetworks.com.au

```html
<!DOCTYPE html>
<html lang="en">
<head>
<meta charset="utf-8">
<title>TQ Networks – Business Card</title>
<link rel="stylesheet" href="https://fonts.googleapis.com/css2?family=Roboto+Condensed:wght@400;700&family=Roboto:wght@400;500&display=swap">
<style>
  :root {
    --stage: #d9d3ca;
    --card-white: #ffffff;
    --brand-red: #e3232b;
    --brand-red-dark: #c4151d;
    --ink-grey: #6b6b6b;
    --text-white: #ffffff;
  }
  html, body {
    margin: 0;
    padding: 0;
    width: 900px;
    height: 1200px;
    overflow: hidden;
    background: var(--stage);
  }
  .canvas {
    position: relative;
    width: 900px;
    height: 1200px;
  }
  .card {
    position: absolute;
    left: 81px;
    width: 735px;
    height: 429px;
    border-radius: 30px;
    box-shadow: 0 10px 24px rgba(0,0,0,0.25);
    overflow: hidden;
  }
  .card--front {
    top: 126px;
    background: var(--card-white);
  }
  .card--back {
    top: 726px;
    background: linear-gradient(160deg, var(--brand-red) 0%, var(--brand-red-dark) 100%);
  }

  /* Front */
  .person {
    position: absolute;
    right: 360px;
    top: 168px;
    text-align: right;
    font-family: "Roboto Condensed", sans-serif;
  }
  .person__name {
    margin: 0;
    font-weight: 700;
    font-size: 25px;
    letter-spacing: 0.5px;
    color: var(--brand-red);
    text-transform: uppercase;
  }
  .person__title {
    margin: 4px 0 0;
    font-size: 19px;
    color: var(--ink-grey);
  }
  .divider {
    position: absolute;
    left: 393px;
    top: 156px;
    width: 2px;
    height: 120px;
    background: var(--brand-red);
  }
  .contact-list {
    position: absolute;
    left: 405px;
    top: 150px;
    margin: 0;
    padding: 0;
    list-style: none;
    font-family: "Roboto", sans-serif;
    font-size: 20px;
    color: var(--brand-red);
  }
  .contact-list li {
    display: flex;
    align-items: center;
    height: 33px;
  }
  .contact-list svg {
    width: 16px;
    height: 16px;
    margin-right: 14px;
    fill: var(--brand-red);
    flex: none;
  }

  /* Back */
  .company-name {
    position: absolute;
    left: 54px;
    top: 60px;
    margin: 0;
    font-family: "Roboto Condensed", sans-serif;
    font-weight: 700;
    font-size: 66px;
    letter-spacing: 1px;
    color: var(--text-white);
    text-transform: uppercase;
  }
  .services {
    position: absolute;
    left: 384px;
    top: 268px;
    margin: 0;
    padding: 0;
    list-style: none;
    font-family: "Roboto", sans-serif;
    font-size: 19px;
    line-height: 27px;
    color: var(--text-white);
    text-transform: uppercase;
  }
  .services li {
    position: relative;
    padding-left: 20px;
  }
  .services li::before {
    content: "";
    position: absolute;
    left: 2px;
    top: 10px;
    width: 7px;
    height: 7px;
    border-radius: 50%;
    background: var(--text-white);
  }
</style>
</head>
<body>
<main class="canvas">
  <section class="card card--front" aria-label="Card front">
    <div class="person">
      <p class="person__name">Dwayne Falstrup</p>
      <p class="person__title">Director</p>
    </div>
    <div class="divider"></div>
    <ul class="contact-list">
      <li>
        <svg viewBox="0 0 24 24" aria-hidden="true"><path d="M6.6 10.8a15.1 15.1 0 0 0 6.6 6.6l2.2-2.2a1 1 0 0 1 1-.25 11.4 11.4 0 0 0 3.6.57 1 1 0 0 1 1 1V20a1 1 0 0 1-1 1A17 17 0 0 1 3 4a1 1 0 0 1 1-1h3.5a1 1 0 0 1 1 1c0 1.25.2 2.45.57 3.57a1 1 0 0 1-.25 1z"/></svg>
        03 6193 4827
      </li>
      <li>
        <svg viewBox="0 0 24 24" aria-hidden="true"><path d="M7 1h10a2 2 0 0 1 2 2v18a2 2 0 0 1-2 2H7a2 2 0 0 1-2-2V3a2 2 0 0 1 2-2zm0 3v14h10V4zm5 15.5a1.2 1.2 0 1 0 0 2.4 1.2 1.2 0 0 0 0-2.4z"/></svg>
        0412 587 239
      </li>
      <li>
        <svg viewBox="0 0 24 24" aria-hidden="true"><path d="M2 5h20v14H2zm2 2v.5l8 5 8-5V7zm0 2.9V17h16V9.9l-8 5z"/></svg>
        dwayne@tqnetworks.com.au
      </li>
      <li>
        <svg viewBox="0 0 24 24" aria-hidden="true"><path d="M12 2a10 10 0 1 0 0 20 10 10 0 0 0 0-20zm6.9 6h-2.9a15.6 15.6 0 0 0-1.4-3.6A8 8 0 0 1 18.9 8zM12 4a14 14 0 0 1 1.9 4h-3.8A14 14 0 0 1 12 4zM4.3 14a8.2 8.2 0 0 1 0-4h3.4a16.5 16.5 0 0 0 0 4zm.8 2h2.9a15.6 15.6 0 0 0 1.4 3.6A8 8 0 0 1 5.1 16zM8 8H5.1a8 8 0 0 1 4.3-3.6A15.6 15.6 0 0 0 8 8zm4 12a14 14 0 0 1-1.9-4h3.8A14 14 0 0 1 12 20zm2.3-6H9.7a14.7 14.7 0 0 1 0-4h4.6a14.7 14.7 0 0 1 0 4zm.3 5.6A15.6 15.6 0 0 0 16 16h2.9a8 8 0 0 1-4.3 3.6zm1.7-5.6a16.5 16.5 0 0 0 0-4h3.4a8.2 8.2 0 0 1 0 4z"/></svg>
        www.tqnetworks.com.au
      </li>
    </ul>
  </section>

  <section class="card card--back" aria-label="Card back">
    <h1 class="company-name">TQ Networks</h1>
    <ul class="services">
      <li>Managed IT Services</li>
      <li>Productivity Solutions</li>
      <li>Data Backup and Recovery</li>
      <li>IT System Maintenance</li>
      <li>Managed IT Security</li>
    </ul>
  </section>
</main>
</body>
</html>
```